Fun and Splashy Flyer Design

We need a flyer designed for our new car cleaning brand! We have looked around, and the stock options either look way too dark/serious/exclusive, or they look too shiny/stock image.

We need something that can be more subtle, that works with our work van.

For this project we would like a photoshop file with individual layers, and you can just put placeholder text for the main slogan, a header 1, header 2, bullet point and body text.

What we're really looking for are the transitions between images and elements, font colours and pairings and design accents.

We want the brand to be fun, clean, happy and straightforward (slightly minimalist). Please message if you have any questions!

```html
<!DOCTYPE html>
<html lang="en">
<head>
<meta charset="utf-8">
<title>Car Wash Services Flyer</title>
<link rel="stylesheet" href="https://fonts.googleapis.com/css2?family=Arimo:wght@400;700&family=Open+Sans:wght@400;600;700&display=swap">
<style>
  :root {
    --page-bg: #dfe2e5;
    --paper: #f7f8f9;
    --navy: #1f3f8f;
    --brand-blue: #2367b5;
    --sky: #5aa6d6;
    --teal: #1f7fa6;
    --dot-navy: #1d2f8c;
    --dot-sky: #3fa0e0;
    --drop-top: #5fb4e8;
    --drop-bottom: #16357a;
    --body-grey: #5b6068;
    --photo-dark: #3b3f46;
    --photo-mid: #6b7079;
    --photo-car: #2f5f86;
  }
  * { margin: 0; padding: 0; box-sizing: border-box; }
  html, body { width: 1200px; height: 799px; overflow: hidden; }
  body { background: var(--page-bg); position: relative; }

  .flyer {
    position: absolute; left: 320px; top: 50px;
    width: 560px; height: 700px;
    background: var(--paper);
    overflow: hidden;
    box-shadow: 0 4px 18px rgba(0,0,0,.18);
    font-family: "Open Sans", sans-serif;
  }
  .hero-photo { position: absolute; left: 0; top: 0; width: 560px; height: 360px; }

  .brand {
    position: absolute; right: 24px; top: 24px;
    display: flex; align-items: center; gap: 8px;
    font-family: "Open Sans", sans-serif; font-weight: 700;
    font-size: 17px; color: var(--navy);
    background: rgba(255,255,255,.85); padding: 6px 12px; border-radius: 20px;
  }
  .brand-dot { width: 16px; height: 16px; border-radius: 50%; background: #f2cf1f; }

  .headline {
    position: absolute; left: 30px; top: 70px;
    font-family: "Arimo", sans-serif; color: #fff; line-height: .95;
    text-shadow: 0 2px 6px rgba(0,0,0,.35);
  }
  .headline .big { display: block; font-weight: 700; font-size: 62px; letter-spacing: 1px; }
  .headline .big.second { padding-left: 28px; }
  .headline .small { display: block; font-size: 30px; padding-left: 88px; margin-top: 4px; }

  .accents { position: absolute; left: 0; top: 340px; width: 300px; height: 160px; }

  .service-drops { position: absolute; left: 24px; top: 372px; display: flex; gap: 8px; }
  .drop { position: relative; width: 84px; height: 104px; }
  .drop svg { position: absolute; inset: 0; }
  .drop span {
    position: absolute; left: 0; right: 0; top: 50px;
    text-align: center; color: #fff; font-size: 13px; line-height: 1.2; font-weight: 600;
  }

  .intro { position: absolute; left: 318px; top: 396px; width: 220px; }
  .intro h2 { font-size: 14px; font-weight: 700; color: var(--brand-blue); margin-bottom: 8px; }
  .intro p { font-size: 10.5px; line-height: 1.45; color: var(--body-grey); }

  .hours {
    position: absolute; left: 30px; top: 488px;
    font-family: "Open Sans", sans-serif; font-weight: 600; font-size: 44px;
    color: var(--sky); line-height: 1;
  }
  .phone {
    position: absolute; left: 34px; top: 534px;
    font-family: "Arimo", sans-serif; font-weight: 700; font-size: 25px; color: var(--navy);
  }
  .slogan {
    position: absolute; left: 30px; top: 590px;
    font-family: "Open Sans", sans-serif; font-weight: 600; font-size: 26px; color: var(--brand-blue);
  }
  .footer-band { position: absolute; left: 0; bottom: 0; width: 560px; height: 70px; }
  .website {
    position: absolute; left: 0; right: 0; bottom: 16px; text-align: center;
    font-size: 22px; color: #fff;
  }
</style>
</head>
<body>
  <main class="flyer">
    <svg class="hero-photo" viewBox="0 0 560 360" role="img" aria-label="Photo of a glove washing a grille with a blue sports car and water splash">
      <defs>
        <linearGradient id="photoTone" x1="0" y1="0" x2="1" y2="1">
          <stop offset="0" stop-color="var(--photo-mid)"/>
          <stop offset=".5" stop-color="var(--photo-dark)"/>
          <stop offset="1" stop-color="var(--photo-car)"/>
        </linearGradient>
      </defs>
      <path d="M0 0 H560 V290 C480 320 400 345 300 342 C200 338 90 318 0 345 Z" fill="url(#photoTone)"/>
    </svg>

    <div class="brand"><span class="brand-dot"></span>Bright Suds</div>

    <h1 class="headline">
      <span class="big">CAR</span>
      <span class="big second">WASH</span>
      <span class="small">services</span>
    </h1>

    <svg class="accents" viewBox="0 0 300 160" aria-hidden="true">
      <circle cx="30" cy="42" r="12" fill="var(--dot-navy)"/>
      <circle cx="56" cy="28" r="7" fill="var(--dot-sky)"/>
      <circle cx="76" cy="44" r="6" fill="var(--dot-sky)"/>
      <circle cx="104" cy="30" r="10" fill="var(--dot-sky)"/>
      <circle cx="178" cy="22" r="10" fill="var(--dot-navy)"/>
      <circle cx="202" cy="12" r="6" fill="var(--dot-sky)"/>
    </svg>

    <div class="service-drops">
      <div class="drop">
        <svg viewBox="0 0 84 104" aria-hidden="true">
          <defs><linearGradient id="dropFill" x1="0" y1="0" x2="0" y2="1"><stop offset="0" stop-color="var(--drop-top)"/><stop offset="1" stop-color="var(--drop-bottom)"/></linearGradient></defs>
          <path d="M42 2 C54 30 80 48 80 68 A38 34 0 0 1 4 68 C4 48 30 30 42 2 Z" fill="url(#dropFill)" stroke="#fff" stroke-width="2"/>
        </svg>
        <span>Engine<br>wash</span>
      </div>
      <div class="drop">
        <svg viewBox="0 0 84 104" aria-hidden="true"><path d="M42 2 C54 30 80 48 80 68 A38 34 0 0 1 4 68 C4 48 30 30 42 2 Z" fill="url(#dropFill)" stroke="#fff" stroke-width="2"/></svg>
        <span>Body<br>Wash</span>
      </div>
      <div class="drop">
        <svg viewBox="0 0 84 104" aria-hidden="true"><path d="M42 2 C54 30 80 48 80 68 A38 34 0 0 1 4 68 C4 48 30 30 42 2 Z" fill="url(#dropFill)" stroke="#fff" stroke-width="2"/></svg>
        <span>Interior<br>Cleaning</span>
      </div>
    </div>

    <section class="intro">
      <h2>Full and express wash services</h2>
      <p>For this project we would like a,and you can put placeholder text for the main slogan, a header 1, header 2, bullet point and body text.What we're really looking for are the transitions between images and elements font colours and pairings and design accents</p>
    </section>

    <p class="hours">OPEN 24/7</p>
    <p class="phone">555-014-2290</p>
    <p class="slogan">It’s More Afforadle Thank you think</p>

    <svg class="footer-band" viewBox="0 0 560 70" aria-hidden="true">
      <path d="M0 70 V40 C150 10 380 0 560 22 V70 Z" fill="var(--teal)"/>
    </svg>
    <p class="website">brightsudsdetail.ca</p>
  </main>
</body>
</html>
```